" Empresa jovem, em franca expansao, com necessidade de ampliar e qualificar sua carteira de clientes, buscando aprimorar sua identidade visual para se destacar em uma concorrência com pouco investimento nesse fundamento corporativo e potencializar sua apresentaçao a clientes de grande porte. "

```html
<!DOCTYPE html>
<html lang="pt-BR">
<head>
<meta charset="utf-8">
<title>Assinatura de e-mail – Afiadora Serrana</title>
<link rel="stylesheet" href="https://fonts.googleapis.com/css2?family=Open+Sans:wght@400;600;700&display=swap">
<style>
  :root {
    --page: #ffffff;
    --brand-light: #f1f3f4;
    --brand-mid: #dfe3e5;
    --navy: #0f2a45;
    --navy-deep: #0a1f35;
    --teal: #1d5a6a;
    --ink-light: #ffffff;
    --ink-soft: #c9d3dd;
  }
  * { box-sizing: border-box; margin: 0; padding: 0; }
  html, body {
    width: 1200px; height: 1200px; overflow: hidden;
    background: var(--page);
    font-family: "Open Sans", Arial, sans-serif;
  }
  .canvas {
    width: 1200px; height: 1200px;
    display: flex; align-items: center; justify-content: center;
  }
  .signature {
    width: 1080px; height: 288px;
    display: flex;
  }
  .brand-panel {
    width: 560px; height: 100%;
    background: linear-gradient(180deg, var(--brand-light) 0%, var(--brand-mid) 100%);
    display: flex; align-items: center; justify-content: center; gap: 22px;
  }
  .brand-mark {
    width: 40px; height: 40px;
    background: var(--teal);
  }
  .brand-name {
    font-size: 44px; font-weight: 700; letter-spacing: 1px;
    color: var(--navy); text-transform: uppercase; line-height: 1;
  }
  .contact-panel {
    flex: 1; height: 100%;
    background: linear-gradient(180deg, var(--navy) 0%, var(--navy-deep) 100%);
    border-top-right-radius: 150px;
    padding: 34px 40px 30px 46px;
    color: var(--ink-light);
  }
  .person-name { font-size: 26px; font-weight: 600; line-height: 1.1; }
  .person-role { font-size: 15px; color: var(--ink-soft); margin-bottom: 22px; }
  .contact-list { list-style: none; }
  .contact-item {
    display: flex; align-items: flex-start; gap: 14px;
    font-size: 15px; line-height: 1.3; color: var(--ink-soft);
    margin-bottom: 9px;
  }
  .contact-icon { width: 18px; height: 18px; flex: none; margin-top: 1px; }
</style>
</head>
<body>
<main class="canvas">
  <section class="signature">
    <div class="brand-panel">
      <span class="brand-mark"></span>
      <span class="brand-name">Afiadora Serrana</span>
    </div>
    <div class="contact-panel">
      <p class="person-name">Paulo Henrique</p>
      <p class="person-role">Diretor</p>
      <ul class="contact-list">
        <li class="contact-item">
          <svg class="contact-icon" viewBox="0 0 24 24"><path fill="#fff" d="M12 2a7 7 0 0 0-7 7c0 5 7 13 7 13s7-8 7-13a7 7 0 0 0-7-7zm0 9.5a2.5 2.5 0 1 1 0-5 2.5 2.5 0 0 1 0 5z"/></svg>
          <span>Rua das Acácias, 410 Centro<br>Serra Alta MG</span>
        </li>
        <li class="contact-item">
          <svg class="contact-icon" viewBox="0 0 24 24"><path fill="#fff" d="M6.6 10.8a15 15 0 0 0 6.6 6.6l2.2-2.2c.3-.3.7-.4 1-.2 1.1.4 2.3.6 3.6.6.6 0 1 .4 1 1V20c0 .6-.4 1-1 1A17 17 0 0 1 3 4c0-.6.4-1 1-1h3.5c.6 0 1 .4 1 1 0 1.3.2 2.5.6 3.6.1.3 0 .7-.2 1z"/></svg>
          <span>31 5555-0142</span>
        </li>
        <li class="contact-item">
          <svg class="contact-icon" viewBox="0 0 24 24"><rect x="2" y="5" width="20" height="14" rx="2" fill="#fff"/><path d="M3 6l9 7 9-7" fill="none" stroke="#0f2a45" stroke-width="2"/></svg>
          <span>contato@serrana.com.br</span>
        </li>
        <li class="contact-item">
          <svg class="contact-icon" viewBox="0 0 24 24"><circle cx="12" cy="12" r="9.5" fill="none" stroke="#fff" stroke-width="2"/><path d="M2.5 12h19M12 2.5c3 3 3 16 0 19M12 2.5c-3 3-3 16 0 19" fill="none" stroke="#fff" stroke-width="1.6"/></svg>
          <span>www.serrana.com.br</span>
        </li>
      </ul>
    </div>
  </section>
</main>
</body>
</html>
```